nutrition company business card

I would like to have a business card that has two sides, one being the green color from the Company name on the logo. I am open to ideas and looks that work with my logo. I like the idea of having a negative image of the tree on the green side.

For my information on the card I must have:
Linda Moorcombe
415-872-6041
lindamoorcombe@quellmail.net

This area will need to be updated once I complete my schooling.

Reason: I need to extend my deadline by one day as I have been sick the last week and not had time to review all the new designs. Thank you.

Industry/Entity Type

Nutrition

Requirements
Must have
• I would like to have a business card that has two sides, one being the green color from the Company name on the logo. I am open to ideas and looks that work with my logo. I like the idea of having a negative image of the tree on the green side.
• For my information on the card I must have:
• Linda Moorcombe
• 415-872-6041
• lindamoorcombe@quellmail.net
• This area will need to be updated once I complete my schooling.

```html
<!DOCTYPE html>
<html lang="en">
<head>
<meta charset="utf-8">
<title>Thriving Tables – Business Card</title>
<link rel="stylesheet" href="https://fonts.googleapis.com/css2?family=Barlow:wght@400;500&family=Quicksand:wght@400&display=swap">
<style>
  :root {
    --green-deep: #4b7520;
    --green-mid: #6c9f2e;
    --green-glow: #7fb236;
    --green-light: #a4c74c;
    --green-soft: #72a630;
    --text-name: #8ec25a;
    --text-contact: #93b866;
    --brand-green: #8dc63f;
    --ring: #a38c8c;
  }
  html, body {
    margin: 0;
    padding: 0;
    width: 1200px;
    height: 768px;
    overflow: hidden;
    background: var(--green-deep);
  }
  .card {
    position: relative;
    width: 1200px;
    height: 768px;
    overflow: hidden;
    background: radial-gradient(ellipse 620px 420px at 560px 330px, var(--green-glow) 0%, var(--green-mid) 45%, var(--green-deep) 100%);
  }
  .card__wave {
    position: absolute;
    inset: 0;
    width: 1200px;
    height: 768px;
  }
  .contact {
    position: absolute;
    top: 36px;
    left: 38px;
    width: 566px;
    font-family: "Barlow", sans-serif;
    text-align: center;
  }
  .contact__name {
    margin: 0;
    font-size: 72px;
    font-weight: 400;
    letter-spacing: 1px;
    line-height: 1.1;
    color: var(--text-name);
  }
  .contact__phone,
  .contact__email {
    margin: 0;
    font-size: 44px;
    font-weight: 500;
    line-height: 1.35;
    color: var(--text-contact);
  }
  .contact__phone { margin-top: 8px; }
  .brand {
    position: absolute;
    top: 18px;
    left: 660px;
    width: 528px;
    text-align: center;
  }
  .brand__ring {
    display: block;
    width: 150px;
    height: 150px;
    margin: 0 auto;
  }
  .brand__name {
    margin: 18px 0 0;
    font-family: "Quicksand", sans-serif;
    font-weight: 400;
    font-size: 50px;
    letter-spacing: 0.5px;
    color: var(--brand-green);
    line-height: 1;
  }
</style>
</head>
<body>
  <main class="card">
    <svg class="card__wave" viewBox="0 0 1200 768" aria-hidden="true">
      <defs>
        <radialGradient id="wave-fill" cx="560" cy="400" r="700" gradientUnits="userSpaceOnUse">
          <stop offset="0" stop-color="#a6c94f"/>
          <stop offset="0.55" stop-color="#80b038"/>
          <stop offset="1" stop-color="#6a9d2b"/>
        </radialGradient>
      </defs>
      <path d="M0,672 C300,430 780,330 1040,333 C1120,335 1170,345 1200,355 L1200,768 L0,768 Z" fill="url(#wave-fill)"/>
      <path d="M0,672 C300,430 780,330 1040,333 C1120,335 1170,345 1200,355" fill="none" stroke="#8fbc45" stroke-width="2" opacity="0.6"/>
    </svg>

    <section class="contact">
      <h1 class="contact__name">Linda Moorcombe</h1>
      <p class="contact__phone">415-872-6041</p>
      <p class="contact__email">lindamoorcombe@quellmail.net</p>
    </section>

    <section class="brand">
      <svg class="brand__ring" viewBox="0 0 150 150" aria-hidden="true">
        <circle cx="75" cy="75" r="72" fill="none" stroke="var(--ring)" stroke-width="4"/>
      </svg>
      <p class="brand__name">Thriving Tables</p>
    </section>
  </main>
</body>
</html>
```